Web Design Project

I need a three page website. I have designed the index.html and the specialevent.html page.

I need someone to finetune the pages for me.

Where I have difficulty is with the following:
I want to add an event table driven by php database.
The administrator of the event will login and create the wording that fits under each colmn. The administrator the submit the form to php database. The database then display in a html.

The Table contains 5 coloums and the rows can vary and can go up to as many as 100.

The table set out events on a program
In the last column of every row I need a submit button to "View and Book" I need to link those buttons with external links/pages.

I use Dreamweaver CS5 and I need to have it in this format in order for me to edit it in the future.

The Table needs to be updated once a year for this program. So ideally if someone has a password to update the certain regions this is what I have in mind.

I have also designed a mockup of the restaurant page. At the top I need.
1) 4 Colapsable panels
a) Restaurants - opening the names of the restaurants
b) Coffee shops and light lunches .... with the names
c) Family
d) Home eateries

From the colapsable panel of each of these I need a anchored link to the description/photos of each...with a BOOK now button I can submit bookings to.

I added a colapsable panel in each restaurants description to keep everything contained.

Please help

• Background must be fixed so that main.div scroll over it

The colours are chosen so please stick to it.

The green for the submit button I short is. #C8D707

I need to edit the pages in Dreamweaver CS5. /Flexilayout2pro

Please ask if you need to know anything. I exactly know what I want.

Kind regards
Marius Dreyer

The colours are fine.

The wording " havenridgeonline BOOKING agent" should appear right at the top in the white horizon part of the background image.

The specialevent page I described already. I am interested in the editable solution. for this.

I will make up a mockup of the third page and send it later.

Regards

```html
<!DOCTYPE html>
<html lang="en">
<head>
<meta charset="utf-8">
<title>havenridgeonline – Harvest festival Program</title>
<link rel="stylesheet" href="https://fonts.googleapis.com/css2?family=Tinos:ital,wght@0,400;0,700;1,700&family=Noto+Sans:wght@400&display=swap">
<style>
  :root{
    --lime:#c8d707;
    --lime-dark:#8f9a05;
    --btn-top:#c6d30c;
    --btn-bottom:#7f8a04;
    --ink:#111111;
    --site-name:#333333;
    --head:#1a1a1a;
    --row:#d9d9d9;
    --panel:#ffffff;
    --footer:#666666;
    --social:#c8c8c8;
    --sep:#777777;
  }
  *{box-sizing:border-box;margin:0;padding:0}
  html,body{width:1200px;height:994px;overflow:hidden}
  body{position:relative;background:var(--footer);font-family:"Noto Sans",Verdana,sans-serif;color:var(--ink)}
  .landscape{position:absolute;left:0;top:0;width:1200px;height:716px;
    background:linear-gradient(180deg,#fbfbfa 0%,#f1f0ec 6%,#a9a79e 12%,#8d8b82 22%,#6f6d63 40%,#7a776c 60%,#8c897f 80%,#9b988e 100%)}
  .site-name{position:absolute;left:197px;top:10px;font-family:"Noto Sans",Verdana,sans-serif;font-size:24px;font-weight:400;color:var(--site-name)}
  .nav{position:absolute;left:182px;top:172px;width:836px;height:42px;border-radius:21px;background:var(--lime);
    box-shadow:0 2px 3px rgba(0,0,0,.35);display:flex;justify-content:center;align-items:center;padding-left:44px}
  .nav a{font-family:"Tinos",serif;font-size:13.5px;color:#fff;text-decoration:none;text-shadow:0 0 2px rgba(0,0,0,.5)}
  .nav a+a{margin-left:30px}
  .nav a.play{margin-right:20px}
  .page-title{position:absolute;left:197px;top:227px;font-family:"Tinos",serif;font-style:italic;font-weight:700;font-size:29px;color:#fff;text-shadow:0 1px 3px rgba(0,0,0,.5)}
  .panel{position:absolute;left:182px;top:287px;width:836px;height:470px;background:var(--panel);border-radius:18px}
  .program{position:absolute;left:13px;top:14px;width:808px}
  .program-row{display:grid;grid-template-columns:303px 144px 97px 103px 161px;align-items:center;height:40px;background:var(--row);margin-bottom:4px;font-size:14.5px}
  .program-row.head{background:var(--head);color:#fff;font-size:17.5px;height:38px;border-radius:8px 8px 0 0;margin-bottom:4px}
  .cell{position:relative;text-align:center}
  .cell:first-child{text-align:left;padding-left:13px}
  .cell+.cell::before{content:"";position:absolute;left:0;top:50%;height:20px;margin-top:-10px;border-left:1px solid var(--sep)}
  .book{display:block;margin-left:auto;margin-right:7px;width:144px;height:27px;border-radius:4px;border:1px solid var(--lime-dark);
    background:linear-gradient(180deg,var(--btn-top),var(--btn-bottom));color:#111;font:14.5px "Noto Sans",Verdana,sans-serif;line-height:25px;text-align:center}
  .footer-contact{position:absolute;left:220px;top:784px;color:#fff;font-family:"Tinos",serif}
  .footer-contact h2{font-size:33px;font-weight:700}
  .phone{font-size:35px;font-weight:700;margin-top:32px}
  .details{font-size:16.5px;line-height:25px;margin-top:24px;width:215px}
  .follow{position:absolute;left:824px;top:784px;color:#fff;font-family:"Tinos",serif}
  .follow h2{font-size:33px;font-weight:700}
  .social{position:absolute;left:816px;top:847px;display:flex;gap:5px}
  .social span{width:38px;height:38px;border-radius:50%;background:var(--social)}
</style>
</head>
<body>
  <div class="landscape" role="img" aria-label="Sepia photograph of a wide valley with mountains, a winding road and a small town in the foreground"></div>
  <div class="site-name">havenridgeonline</div>
  <nav class="nav">
    <a href="#">Home</a><a href="#">Accommodation</a><a href="#" class="play">Play</a><a href="#">Contact</a>
  </nav>
  <h1 class="page-title">Harvest festival Program</h1>

  <main class="panel">
    <div class="program">
      <div class="program-row head"><div class="cell">Description</div><div class="cell">Date</div><div class="cell">Time</div><div class="cell">Price</div><div class="cell">Availability</div></div>
      <div class="program-row"><div class="cell">Jewellery design -2day workshop</div><div class="cell">Friday 2 August</div><div class="cell">14h-16h</div><div class="cell">R200pp</div><div class="cell"><span class="book">Availibility Button</span></div></div>
      <div class="program-row"><div class="cell">Cupcake fun</div><div class="cell">Friday 2 August</div><div class="cell">14h-16h</div><div class="cell">R200pp</div><div class="cell"><span class="book">Availibility Button</span></div></div>
      <div class="program-row"><div class="cell">Olive dance</div><div class="cell">Friday 2 August</div><div class="cell">14h-16h</div><div class="cell">R200pp</div><div class="cell"><span class="book">Availibility Button</span></div></div>
      <div class="program-row"><div class="cell">Jewellery design -2day workshop</div><div class="cell">Friday 2 August</div><div class="cell">14h-16h</div><div class="cell">R200pp</div><div class="cell"><span class="book">Availibility Button</span></div></div>
      <div class="program-row"><div class="cell">Cupcake fun</div><div class="cell">Friday 2 August</div><div class="cell">14h-16h</div><div class="cell">R200pp</div><div class="cell"><span class="book">Availibility Button</span></div></div>
      <div class="program-row"><div class="cell">Olive dance</div><div class="cell">Friday 2 August</div><div class="cell">14h-16h</div><div class="cell">R200pp</div><div class="cell"><span class="book">Availibility Button</span></div></div>
      <div class="program-row"><div class="cell">Cupcake fun</div><div class="cell">Friday 2 August</div><div class="cell">14h-16h</div><div class="cell">R200pp</div><div class="cell"><span class="book">Availibility Button</span></div></div>
      <div class="program-row"><div class="cell">Olive dance</div><div class="cell">Friday 2 August</div><div class="cell">14h-16h</div><div class="cell">R200pp</div><div class="cell"><span class="book">Availibility Button</span></div></div>
    </div>
  </main>

  <footer>
    <div class="footer-contact">
      <h2>Contact Us</h2>
      <div class="phone">0861 302710</div>
      <div class="details">email: admin@hronline.biz<br>address: Mill Street, Havenridge</div>
    </div>
    <div class="follow"><h2>Follow Us</h2></div>
    <div class="social" aria-label="Social links"><span></span><span></span><span></span><span></span></div>
  </footer>
</body>
</html>
```